Alternative Country Rock Band Needs Website Design

Milo R and The Drifthands Web Design Proposal

Overview
We essentially need design and code for an uncluttered, easy to navigate, simple to access repository for our music, videos, photos, up and coming shows, merchandise, and links to social media. It will be a platform for our fans, new and old to get to the heart of who we are and what we are doing. We want something that will embody our essence as musicians, our distinct flavor, and values. We must be able to add, remove and edit content without developer help.

*If we receive a design so good that it justifies no code, we are open to that*

Friendloop
It would be nice to have Friendloop integration so that much of the site can be liked, possibly commented on but most importantly shared.

This could also possibly be done on Swirlpad http://www.swirlpad.example/ which posts right to Chirpline feeds and Friendloop with cross links back.

Smart Phone
We need the site to be compatible with smart phones.

Branding/Aesthetics

We are really keen on aesthetics. We are almost more concerned about the feel of the site than content, which of course will be there.

We want to aim at an edgy, gritty, folky rock ‘n’ roll with a cowboy kick ambiance. We want the space to have a Southwestern romanticism risqué tinge. We want something that feels similar to our new EP album cover “Dust On Gold.”

Our image is huge and we want people, agents, managers, venues, friends, family, and fans to see who we are immediately and be able to easily connect to us, share us, and contact us.

Content

Our EchoDistrict and Friendloop already exists, so much of it can essentially be reworked into the new site.

We want an About; Shows; Music; Videos (maybe combine as just “Music” so that we don’t clutter the site); Photos; Media/Press (one of the two); Store; Contact Us (booking inquiries etc.) and Easy Big Connectors to Social Media; Email List (somewhere, probably not in navigation)

Examples

These are band sites that we think more or less hit the nail on the head. When reviewing them, it seems we are drawn to sites that have very large pictures, large, easy to use navigation buttons and such.

http://paulvantross.example/

http://www.harborandkin.example/

http://thegreyheron.example/

http://www.mavelinsound.example/site/

http://www.thecrookedpath.example/ (love the size of the photos but don’t like the small navigation)

Hosting
Nimbra has been recommended and it is free, but let us know if you know a better one.

Content Management
We want to be able to upload our shows using EchoDistrict and that they will show on our website, likely by using an RSS Feed. It might even be nice if music, photos and videos could also be linked. Basic Ruby on Rails has been recommended for content management, making it easier to add and remove content, but maybe you know better.

However, we are open to Block Frame or Zop as a prefabricated content management system as well.

Latest Technologies
We need the site up to date with the latest technologies out there, rss feeds, and so on so it will show up on search engines.
Updates

Project Deadline Extended
Reason: A number of designers accepted the job and are yet to submit their work.

Project Deadline Extended
Reason: We are looking for some original design elements. It seems many have over utilized our pictures to supplement design. We've added another $200 on top of the original $300 for a total of $500 for the project. We look forward to your participation!

We've added $200 to bring the total to $500 for our web design.  We are looking forward to your ideas...

Hi Designers,

We've added some more band pictures and posters for inspiration for possible designs.  We look forward to your submissions!

Milo R

Industry/Entity Type

Store

Font styles to use
Sans Serif
Decorative

```html
<!DOCTYPE html>
<html lang="en">
<head>
<meta charset="utf-8">
<title>Milo R and The Drifthands — Contact</title>
<link href="https://fonts.googleapis.com/css2?family=Alfa+Slab+One&family=Arimo&display=swap" rel="stylesheet">
<style>
  :root {
    --page-bg: #e9e8e4;
    --band-light: #7a6040;
    --band-dark: #5a4428;
    --body-light: #5c4529;
    --body-dark: #3f2e1a;
    --cream: #dcd0b2;
    --field-fill: #d3c9b0;
    --field-edge: #6e583a;
    --field-text: #7d7462;
    --button-fill: #4a3416;
    --button-edge: #cbbb96;
  }
  * { box-sizing: border-box; margin: 0; padding: 0; }
  html, body { width: 1200px; height: 1000px; overflow: hidden; background: var(--page-bg); }
  .site {
    position: absolute; left: 0; top: 199px; width: 1200px; height: 602px;
    background:
      radial-gradient(ellipse at 30% 40%, rgba(120,90,50,.35), transparent 60%),
      radial-gradient(ellipse at 80% 80%, rgba(30,20,10,.35), transparent 55%),
      linear-gradient(180deg, var(--body-light), var(--body-dark));
    box-shadow: 0 2px 8px rgba(0,0,0,.35);
    font-family: "Arimo", Arial, sans-serif;
  }
  .nav-band {
    position: absolute; left: 0; top: 0; width: 100%; height: 105px;
    background:
      radial-gradient(ellipse at 50% 60%, rgba(160,120,70,.45), transparent 70%),
      linear-gradient(180deg, var(--band-light), var(--band-dark));
    border-bottom: 1px solid rgba(40,28,14,.5);
  }
  .nav { position: absolute; left: 250px; top: 24px; display: flex; gap: 22px; list-style: none; }
  .nav li { position: relative; font-family: "Alfa Slab One", Georgia, serif; font-size: 20px; color: var(--cream); letter-spacing: .5px; }
  .nav li.active { color: #f3ecd9; }
  .nav .chevron { position: absolute; left: 50%; top: 30px; transform: translateX(-50%); }
  .heading { position: absolute; top: 233px; font-family: "Alfa Slab One", Georgia, serif; font-size: 19px; color: var(--cream); letter-spacing: .5px; }
  .field {
    position: absolute; background: var(--field-fill); border: 2px solid var(--field-edge);
    color: var(--field-text); font-size: 18px; padding: 8px 12px; letter-spacing: .5px;
  }
  .send {
    position: absolute; left: 451px; top: 499px; width: 234px; height: 41px;
    background: var(--button-fill); border: 1.5px solid var(--button-edge);
    color: var(--cream); font-size: 18px; letter-spacing: 1px;
    display: flex; align-items: center; justify-content: center;
  }
  .divider { position: absolute; left: 859px; top: 231px; width: 3px; height: 358px; background: var(--cream); border-radius: 2px; }
  .social { position: absolute; width: 76px; height: 76px; border: 2px solid var(--cream); border-radius: 50%;
    display: flex; align-items: center; justify-content: center;
    font-family: "Alfa Slab One", Georgia, serif; font-size: 11px; color: var(--cream); }
</style>
</head>
<body>
  <main class="site">
    <header class="nav-band">
      <ul class="nav">
        <li>ABOUT</li><li>SHOWS</li><li>MUSIC</li><li>PHOTOS</li><li>PRESS</li><li>STORE</li>
        <li class="active">CONTACT
          <svg class="chevron" width="34" height="16" viewBox="0 0 34 16" aria-hidden="true">
            <polyline points="2,2 17,13 32,2" fill="none" stroke="#e8dec6" stroke-width="2"/>
            <polyline points="8,2 17,8 26,2" fill="none" stroke="#e8dec6" stroke-width="2"/>
          </svg>
        </li>
      </ul>
    </header>

    <h2 class="heading" style="left:325px">CONTACT US</h2>
    <div class="field" style="left:325px;top:290px;width:234px;height:40px">NAME</div>
    <div class="field" style="left:580px;top:290px;width:234px;height:40px">E-MAIL</div>
    <div class="field" style="left:324px;top:357px;width:490px;height:117px">MESSAGE</div>
    <div class="send">SEND</div>

    <div class="divider"></div>

    <h2 class="heading" style="left:914px">LINKS</h2>
    <div class="social" style="left:900px;top:291px">Friendloop</div>
    <div class="social" style="left:994px;top:291px">Chirpline</div>
    <div class="social" style="left:1087px;top:291px;font-size:9px">EchoDistrict</div>
    <div class="social" style="left:900px;top:383px">Vidreel</div>
    <div class="social" style="left:994px;top:383px">Framecast</div>
    <div class="social" style="left:1087px;top:383px">Tunestall</div>
  </main>
</body>
</html>
```